eBook opt in for website

I write short ebooks (2500 words) to give free as an opt in. I need a cover design with block headers within the pages to highlight the specifics sections for PDF.
Book Title:
Bridgeway Mentoring
Sharpen Your Crew Guidance Using Five Simple Habits
I would like to see a design for the front cover that would emphasize a leader's personal growth to team.
The color that comes to mind is blue.
I do have a Brand Design and Icon if you need it.

Leaders with Team Responsibility
Business Consultant

```html
<!DOCTYPE html>
<html lang="en">
<head>
<meta charset="utf-8">
<title>Bridgeway Mentoring – eBook Cover</title>
<link href="https://fonts.googleapis.com/css2?family=Questrial&display=swap" rel="stylesheet">
<style>
  :root {
    --backdrop: #ececec;
    --slate: #4a5163;
    --accent-gold: #f5c518;
    --cover-white: #ffffff;
    --photo-light: #f4ede4;
    --photo-warm: #d9a77e;
    --photo-cool: #5c6a86;
  }
  * { box-sizing: border-box; margin: 0; padding: 0; }
  html, body {
    width: 1200px; height: 800px; overflow: hidden;
    background: var(--backdrop);
    font-family: "Questrial", "Helvetica Neue", Arial, sans-serif;
  }
  .canvas {
    position: relative; width: 1200px; height: 800px;
    display: flex; align-items: center; justify-content: center;
  }
  .cover {
    position: relative; width: 480px; height: 720px;
    background: var(--slate); color: var(--cover-white);
    overflow: hidden;
  }
  .cover__spine-stripe {
    position: absolute; left: 4px; top: 0; bottom: 0; width: 8px;
    background: var(--accent-gold);
  }
  .cover__title {
    position: absolute; left: 28px; top: 12px;
    font-size: 66px; line-height: 78px; font-weight: 400;
    letter-spacing: 0.5px; text-transform: uppercase;
  }
  .cover__title span { display: block; }
  .cover__photo {
    position: absolute; left: 12px; right: 0; top: 180px; height: 324px;
    background:
      radial-gradient(ellipse at 45% 55%, var(--photo-warm) 0%, rgba(217,167,126,0.6) 30%, transparent 60%),
      linear-gradient(110deg, var(--photo-light) 0%, #efe2d2 40%, #c9c6cc 70%, var(--photo-cool) 100%);
  }
  .cover__rule {
    position: absolute; left: 12px; right: 0; top: 504px; height: 5px;
    background: var(--accent-gold);
  }
  .cover__subtitle {
    position: absolute; left: 30px; top: 534px;
    font-size: 25px; line-height: 36px;
  }
  .cover__author {
    position: absolute; left: 30px; top: 640px;
    font-size: 44px; line-height: 52px; letter-spacing: 0.5px;
    text-transform: uppercase;
  }
  .cover__brand {
    position: absolute; right: 18px; top: 600px;
    display: flex; align-items: center; gap: 6px;
    font-size: 12px; color: var(--accent-gold);
  }
  .cover__brand-dot {
    width: 10px; height: 10px; border-radius: 50%;
    background: var(--accent-gold);
  }
</style>
</head>
<body>
  <main class="canvas">
    <article class="cover">
      <div class="cover__spine-stripe"></div>
      <h1 class="cover__title"><span>Bridgeway</span><span>Mentoring</span></h1>
      <div class="cover__photo" role="img" aria-label="Photo of team members stacking their hands together in a bright office"></div>
      <div class="cover__rule"></div>
      <p class="cover__subtitle">Sharpen Your Crew Guidance<br>Using Five Simple Habits</p>
      <div class="cover__brand"><span class="cover__brand-dot"></span>Whitfield Coaching</div>
      <p class="cover__author">Dana Whitfield</p>
    </article>
  </main>
</body>
</html>
```